WWW.VELTRONA.IT BUSINNES CARD

WE NEED A BUSINESS CARD . I HAVE A COMPANY IN ITALY NR 1 IN HAIR MEDICAL CARE AN HAIR REPLECEMENT . IN CARD I NEED WRITE WEB ADDRESS, MAIL , ADDRESS, TELEPHONE NUMBER , AND NAME
IN THE BACK SIDE I NEED MY DOCTOR LOGO .
MY WEB SITE IS WWW.VELTRONA.IT
Updates

Target Market(s)

CONSUMER B2C

Industry/Entity Type

Hair And Beauty

Contact Information for Business Card

I WANT A MEDICAL BUSINESS CARD.

Font styles to use
Other font styles liked:
• VERDANA

Colors
33a6d7
3176b5
85abd2
aedbee
eaf1f7
ffffff

Requirements
Must have
• I NEED MY LOGO AND LOGO OF DR VELTRONA

```html
<!DOCTYPE html>
<html lang="it">
<head>
<meta charset="utf-8">
<title>Veltrona – Business Card</title>
<link rel="stylesheet" href="https://fonts.googleapis.com/css2?family=Montserrat:wght@400;500;600;700&display=swap">
<style>
  :root {
    --navy: #0f5499;
    --blue: #3176b5;
    --sky: #33a6d7;
    --pale: #aedbee;
    --ink: #2b2b33;
    --white: #ffffff;
    --stage: #2a2a2c;
    --hair: #8a5234;
    --skin: #f3c4a6;
  }
  * { margin: 0; padding: 0; box-sizing: border-box; }
  html, body { width: 1200px; height: 848px; overflow: hidden; }
  body {
    background: var(--stage);
    font-family: "Montserrat", Verdana, sans-serif;
    display: flex;
    align-items: center;
    justify-content: center;
    gap: 40px;
  }
  .card {
    position: relative;
    width: 560px;
    height: 320px;
    background: var(--white);
    overflow: hidden;
    box-shadow: 0 10px 30px rgba(0,0,0,.45);
  }
  .card svg.decor { position: absolute; inset: 0; }

  /* back side */
  .back .site-vertical {
    position: absolute;
    right: 10px;
    top: 60px;
    writing-mode: vertical-rl;
    color: var(--white);
    font-size: 13px;
    letter-spacing: 1px;
  }
  .back .doctor-name {
    position: absolute;
    left: 230px;
    top: 58px;
    color: var(--blue);
    font-weight: 700;
    font-size: 20px;
  }
  .back .mascot {
    position: absolute;
    left: 150px;
    top: 95px;
    width: 290px;
    height: 140px;
    border-radius: 14px;
    background: linear-gradient(120deg, rgba(138,82,52,.28), rgba(243,196,166,.35));
  }

  /* front side */
  .front .brand {
    position: absolute;
    left: 40px;
    top: 132px;
  }
  .brand .mark {
    display: flex;
    align-items: center;
    gap: 8px;
    color: var(--navy);
    font-weight: 700;
    font-size: 30px;
    line-height: 36px;
    letter-spacing: .5px;
  }
  .brand .dot {
    width: 20px; height: 20px;
    border-radius: 50%;
    background: var(--sky);
  }
  .brand .tagline {
    margin-top: 4px;
    color: var(--sky);
    font-size: 8.5px;
    font-weight: 600;
    letter-spacing: .3px;
  }
  .front .divider {
    position: absolute;
    left: 285px;
    width: 1.5px;
    background: var(--blue);
  }
  .front .divider.top { top: 50px; height: 36px; }
  .front .divider.bottom { top: 100px; height: 60px; }
  .front .person {
    position: absolute;
    left: 300px;
    top: 40px;
  }
  .person .name {
    color: var(--navy);
    font-weight: 600;
    font-size: 24px;
    letter-spacing: .5px;
  }
  .person .role {
    color: var(--ink);
    font-size: 14px;
    margin-top: 2px;
  }
  .contacts {
    list-style: none;
    margin-top: 10px;
    color: var(--ink);
    font-size: 13.5px;
  }
  .contacts li {
    display: flex;
    align-items: center;
    gap: 8px;
    line-height: 22px;
  }
  .contacts svg { width: 12px; height: 12px; fill: var(--blue); flex: none; }
</style>
</head>
<body>

  <section class="card back">
    <svg class="decor" viewBox="0 0 560 320" width="560" height="320">
      <path d="M485 0 C525 90 470 210 535 320 L560 320 L560 0 Z" fill="var(--navy)"/>
      <path d="M485 0 C525 90 470 210 535 320" fill="none" stroke="var(--sky)" stroke-width="3"/>
    </svg>
    <div class="site-vertical">www.veltrona.com</div>
    <div class="doctor-name">dr. Veltrona</div>
    <div class="mascot" role="img" aria-label="Doctor mascot illustration"></div>
  </section>

  <section class="card front">
    <svg class="decor" viewBox="0 0 560 320" width="560" height="320">
      <path d="M45 252 C130 238 230 215 262 168" fill="none" stroke="var(--sky)" stroke-width="1.5"/>
      <path d="M0 320 C110 215 260 285 400 200 C480 150 530 110 560 70 L560 320 Z" fill="var(--sky)"/>
      <path d="M0 320 L20 320 C130 240 270 300 410 215 C485 168 530 125 560 92 L560 320 Z" fill="var(--navy)"/>
    </svg>

    <div class="brand">
      <div class="mark"><span class="dot"></span>Veltrona</div>
      <div class="tagline">CURA E REINTEGRAZIONE DEI CAPELLI</div>
    </div>

    <span class="divider top"></span>
    <span class="divider bottom"></span>

    <div class="person">
      <div class="name">MARCO ROSSI</div>
      <div class="role">Founder &amp; CEO</div>
      <ul class="contacts">
        <li><svg viewBox="0 0 24 24"><path d="M6.6 10.8a15.1 15.1 0 0 0 6.6 6.6l2.2-2.2a1 1 0 0 1 1-.25 11.4 11.4 0 0 0 3.6.6 1 1 0 0 1 1 1V20a1 1 0 0 1-1 1A17 17 0 0 1 3 4a1 1 0 0 1 1-1h3.5a1 1 0 0 1 1 1c0 1.25.2 2.45.6 3.6a1 1 0 0 1-.25 1z"/></svg>123 555 0142</li>
        <li><svg viewBox="0 0 24 24"><path d="M2 5h20v14H2z M2 5l10 8 10-8"/></svg>rossi@veltrona.com</li>
        <li><svg viewBox="0 0 24 24"><circle cx="12" cy="12" r="10"/></svg>www.veltrona.com</li>
      </ul>
    </div>
  </section>

</body>
</html>
```